Awaken the Quiet Summit is a guide to help individuals overcome obstacles that they face in their life. This book provides thought provoking concepts that allow individuals to work through challenges if their life. The cover needs to be powerful! It needs to speak to the reader of breaking free of problems and overcoming challenges.

Awaken The Quiet Summit
A Map for climbing past hardship and stepping toward the self you were always built to become.
By
Dr. Merrick T. Halvorsby

Industry/Entity Type

Work

```html
<!DOCTYPE html>
<html lang="en">
<head>
<meta charset="utf-8">
<title>Awaken The Quiet Summit — Book Cover Wrap</title>
<link rel="stylesheet" href="https://fonts.googleapis.com/css2?family=Cinzel:wght@400;700&family=PT+Sans+Narrow:wght@400;700&display=swap">
<style>
  :root {
    --navy-deep: #07132b;
    --navy-mid: #0f2a55;
    --navy-light: #17427c;
    --title-crimson: #b3164f;
    --title-shadow: #05070d;
    --ink-white: #ffffff;
    --sky-top: #0a1733;
    --sky-low: #2a63a8;
    --sea: #2f6f9e;
    --surf: #c9dbe6;
    --sand: #c8ab82;
  }
  * { margin: 0; padding: 0; box-sizing: border-box; }
  html, body { width: 1200px; height: 900px; overflow: hidden; background: var(--navy-deep); }

  .cover-wrap {
    position: relative;
    width: 1200px;
    height: 900px;
    overflow: hidden;
    font-family: "PT Sans Narrow", "Arial Narrow", sans-serif;
    color: var(--ink-white);
  }

  /* Back cover + spine share one dark field */
  .back-field {
    position: absolute;
    left: 0; top: 0;
    width: 632px; height: 900px;
    background: linear-gradient(180deg, var(--navy-deep) 0%, var(--navy-mid) 55%, var(--navy-light) 100%);
  }

  .back-copy {
    position: absolute;
    left: 45px;
    width: 460px;
    text-align: center;
    font-size: 20px;
    line-height: 31px;
  }
  .back-copy--blurb { top: 198px; }
  .back-copy--profile { top: 596px; }
  .profile-heading {
    font-size: 18px;
    line-height: 26px;
    margin-bottom: 4px;
  }

  /* Spine */
  .spine-title {
    position: absolute;
    left: 588px; top: 84px;
    height: 680px;
    writing-mode: vertical-rl;
    font-family: "Cinzel", "Trajan Pro", serif;
    font-size: 40px;
    line-height: 44px;
    color: var(--title-crimson);
    white-space: nowrap;
  }
  .spine-rule {
    position: absolute;
    left: 583px; top: 66px;
    width: 3px; height: 708px;
    background: var(--ink-white);
  }
  .spine-subtitle {
    position: absolute;
    left: 540px; top: 88px;
    height: 670px;
    writing-mode: vertical-rl;
    font-size: 17px;
    line-height: 20px;
    text-transform: uppercase;
  }
  .spine-author {
    position: absolute;
    left: 536px; top: 802px;
    width: 96px;
    text-align: center;
    font-size: 17px;
    line-height: 22px;
    letter-spacing: 0.5px;
    text-transform: uppercase;
  }

  /* Front cover */
  .front-photo {
    position: absolute;
    left: 632px; top: 0;
    width: 568px; height: 900px;
  }
  .front-title {
    position: absolute;
    left: 632px; top: 100px;
    width: 568px;
    text-align: center;
    font-family: "Cinzel", "Trajan Pro", serif;
    font-weight: 400;
    font-size: 86px;
    line-height: 72px;
    color: var(--title-crimson);
    text-shadow: 4px 4px 2px var(--title-shadow), 6px 6px 6px rgba(0,0,0,0.6);
  }
  .front-rule {
    position: absolute;
    left: 656px; top: 348px;
    width: 524px; height: 3px;
    background: var(--ink-white);
  }
  .front-subtitle {
    position: absolute;
    left: 648px; top: 360px;
    width: 536px;
    text-align: center;
    font-size: 28px;
    line-height: 32px;
    letter-spacing: 1px;
    text-transform: uppercase;
    text-shadow: 2px 2px 2px rgba(0,0,0,0.7);
  }
  .front-author {
    position: absolute;
    left: 632px; top: 842px;
    width: 568px;
    text-align: center;
    font-size: 46px;
    line-height: 54px;
    letter-spacing: 1px;
    text-transform: uppercase;
    text-shadow: 2px 2px 3px rgba(0,0,0,0.7);
  }
</style>
</head>
<body>
<main class="cover-wrap">

  <section class="back-cover" aria-label="Back cover">
    <div class="back-field"></div>
    <p class="back-copy back-copy--blurb">Awaken the Quiet Summit is a guide to help individuals overcome obstacles that they face in their life. This book provides thought provoking concepts that allow individuals to work through challenges if their life. The cover needs to be powerful! It needs to speak to the reader of breaking free of problems and overcoming challenges.</p>
    <div class="back-copy back-copy--profile">
      <h2 class="profile-heading">AUTHOR’S PROFILE</h2>
      <p>Awaken the Quiet Summit is a guide to help individuals overcome obstacles that they face in their life. This book provides thought provoking concepts that allow individuals to work through challenges if their life. The cover needs to be</p>
    </div>
  </section>

  <section class="spine" aria-label="Spine">
    <h2 class="spine-title">Awaken The Quiet Summit</h2>
    <div class="spine-rule"></div>
    <p class="spine-subtitle">A Map for climbing past hardship and stepping toward the self you were always built to become</p>
    <p class="spine-author">Dr.<br>Merrick<br>T. Halvorsby</p>
  </section>

  <section class="front-cover" aria-label="Front cover">
    <svg class="front-photo" viewBox="0 0 568 900" role="img" aria-label="Photograph: a woman leaping along a beach holding a bunch of colourful balloons under a deep blue sky">
      <defs>
        <linearGradient id="sky" x1="0" y1="0" x2="0" y2="1">
          <stop offset="0" stop-color="var(--sky-top)"/>
          <stop offset="0.45" stop-color="#0f2b5e"/>
          <stop offset="1" stop-color="var(--sky-low)"/>
        </linearGradient>
        <linearGradient id="shore" x1="0" y1="0" x2="0" y2="1">
          <stop offset="0" stop-color="var(--sea)"/>
          <stop offset="0.35" stop-color="var(--surf)"/>
          <stop offset="1" stop-color="var(--sand)"/>
        </linearGradient>
      </defs>
      <rect x="0" y="0" width="568" height="790" fill="url(#sky)"/>
      <rect x="0" y="790" width="568" height="110" fill="url(#shore)"/>
    </svg>
    <h1 class="front-title">Awaken The<br>Quiet<br>Summit</h1>
    <div class="front-rule"></div>
    <p class="front-subtitle">A Map for climbing past hardship and stepping toward the self you were always built to become</p>
    <p class="front-author">Dr. Merrick T. Halvorsby</p>
  </section>

</main>
</body>
</html>
```